Haverill’s

I would like a high class looking card with my logo and contact details (as per uploaded) Elegant, professional and highest quality feel

The following text included …..
“All commercial and residential painting work, large or small. Highest quality finishes and service.”

Industry/Entity Type

Painting

Contact Information for Business Card

Name, phone number, address, email address, company logo

Requirements
Must have
• Double sided

```html
<!DOCTYPE html>
<html lang="en">
<head>
<meta charset="utf-8">
<title>Haverill’s – Business Card</title>
<link rel="stylesheet" href="https://fonts.googleapis.com/css2?family=Cinzel:wght@400&family=Open+Sans:wght@400;700&display=swap">
<style>
  :root {
    --backdrop: #232323;
    --charcoal: #282a2a;
    --gold: #b07f43;
    --gold-light: #c0904f;
    --gold-dark: #9c6e37;
    --white: #ffffff;
    --swoosh: #8a8c8e;
  }
  * { margin: 0; padding: 0; box-sizing: border-box; }
  html, body {
    width: 1200px; height: 780px; overflow: hidden;
    background: var(--backdrop);
  }
  .canvas { position: relative; width: 1200px; height: 780px; }

  .card {
    position: absolute;
    width: 560px; height: 320px;
    overflow: hidden;
    box-shadow: 0 12px 30px rgba(0,0,0,.55);
  }

  /* Front */
  .card--front { left: 40px; top: 50px; }
  .front-texture {
    position: absolute; inset: 0;
    background: linear-gradient(160deg, var(--gold-light) 0%, var(--gold) 50%, var(--gold-dark) 100%);
  }
  .brand {
    position: absolute; left: 0; right: 0; top: 128px;
    display: flex; align-items: center; justify-content: center; gap: 20px;
  }
  .brand-name {
    font-family: "Cinzel", serif;
    font-weight: 400;
    font-size: 50px;
    letter-spacing: 2px;
    color: var(--white);
    line-height: 1;
  }
  .brand-mark {
    width: 62px; height: 62px;
    border: 2px solid var(--white);
    border-radius: 50%;
  }

  /* Back */
  .card--back { left: 600px; top: 410px; background: var(--charcoal); }
  .back-shapes { position: absolute; inset: 0; }
  .owner {
    position: absolute; right: 236px; top: 138px;
    text-align: right;
    font-family: "Open Sans", sans-serif;
  }
  .owner-name { font-weight: 700; font-size: 32px; color: var(--gold); line-height: 1.1; }
  .owner-role { font-weight: 400; font-size: 18px; color: var(--white); }
  .divider {
    position: absolute; left: 340px; top: 62px;
    width: 2px; height: 128px; background: var(--white);
  }
  .contact {
    position: absolute; left: 356px; top: 58px;
    font-family: "Open Sans", sans-serif;
    font-size: 14px; color: var(--white); line-height: 1.4;
  }
  .contact-address { margin-bottom: 8px; }
  .contact-row { display: flex; align-items: center; gap: 7px; }
  .contact-row svg { width: 13px; height: 13px; flex: none; }
  .tagline {
    position: absolute; left: 30px; right: 30px; top: 262px;
    text-align: center;
    font-family: "Open Sans", sans-serif;
    font-size: 16px; color: var(--white); line-height: 1.4;
  }
</style>
</head>
<body>
<main class="canvas">

  <section class="card card--front" aria-label="Business card front">
    <div class="front-texture" role="img" aria-label="Gold background with a repeating pattern of small brand emblems"></div>
    <div class="brand">
      <span class="brand-name">HAVERILL’S</span>
      <span class="brand-mark"></span>
    </div>
  </section>

  <section class="card card--back" aria-label="Business card back">
    <svg class="back-shapes" width="560" height="320" viewBox="0 0 560 320">
      <path d="M0,250 Q420,250 560,185 L560,320 L0,320 Z" fill="var(--gold)"/>
      <path d="M40,243 Q420,246 552,176 Q415,238 40,243 Z" fill="var(--swoosh)"/>
    </svg>

    <div class="owner">
      <div class="owner-name">Tom Haverill</div>
      <div class="owner-role">Owner</div>
    </div>

    <div class="divider"></div>

    <div class="contact">
      <div class="contact-address">42 Kowhai Terrace,<br>Ashbury, 5180</div>
      <div class="contact-row">
        <svg viewBox="0 0 24 24"><path fill="var(--gold)" d="M6.6 10.8a15 15 0 0 0 6.6 6.6l2.2-2.2a1 1 0 0 1 1-.25 11.4 11.4 0 0 0 3.6.57 1 1 0 0 1 1 1V20a1 1 0 0 1-1 1A17 17 0 0 1 3 4a1 1 0 0 1 1-1h3.5a1 1 0 0 1 1 1c0 1.25.2 2.45.57 3.570a1 1 0 0 1-.25 1z"/></svg>
        <span>021 555 0147</span>
      </div>
      <div class="contact-row">
        <svg viewBox="0 0 24 24"><circle cx="12" cy="12" r="9" fill="none" stroke="var(--gold)" stroke-width="2.4"/><path d="M3 12h18M12 3c3 3 3 15 0 18M12 3c-3 3-3 15 0 18" fill="none" stroke="var(--gold)" stroke-width="1.8"/></svg>
        <span>www.haverillpaint.co</span>
      </div>
      <div class="contact-row">
        <svg viewBox="0 0 24 24"><rect x="2" y="5" width="20" height="14" rx="1" fill="none" stroke="var(--gold)" stroke-width="2.4"/><path d="M2 6l10 7 10-7" fill="none" stroke="var(--gold)" stroke-width="2.2"/></svg>
        <span>tom@haverillpaint.co</span>
      </div>
    </div>

    <p class="tagline">All commercial and residential painting work,<br>large or small. Highest quality finishes and service</p>
  </section>

</main>
</body>
</html>
```